iLUMO Brochure

We are looking to create an 11 x 17 bifold brochure on iLUMO. We need an electronic version of the brochure for our web site and also need to be able to have a print format as well. The printed version needs to bleed digital out. The content for the brochure is attached.

FYI - within the attached doc, [notes in square brackets are instructions to designer, NOT part of the text].

Reason: Wanted to extend to provide accurate revisions.

Target Market(s)

Broker Dealers or RIA

Industry/Entity Type

Electronic

Requirements
Must have
• Brand Specifications

Colors
Dark Blue: C: 100, M: 96; Y: 31; K: 26 – R: 35; G: 40: B: 94
Light Blue: C: 77, M: 26; Y: 11; K: 0 – R: 26; G: 151: B: 195

Full color concept photographs with only the above builds as accent colors. Black should be used sparingly, such as in body copy where builds are unmanageable,not as an accent.

Fonts
All fonts for printed materials should remain within the Helvetic or Arial families,unless large quantities of body copy are used, in which case a standard, easily read serif font, such as Times New Roman should be used for body copy. Headings will remain Helvetica or Arial.

Logo Placement
On printed materials the logo should appear at the bottom of the page (unless it is not appropriate within context) on a horizontal bar that graduates from the standard “light blue” to white. The logo should appear on the white end of the bar and contact information on the other end of the bar. The “dark blue” color build should be used for the contact information, which will be in Helvetica or Arial according to the font standards.

Paper and background
Paper stock selected should be bright cool white.

```html
<!DOCTYPE html>
<html lang="en">
<head>
<meta charset="utf-8">
<title>iLUMO Automated Workflow Brochure</title>
<link href="https://fonts.googleapis.com/css2?family=Arimo:wght@400;700&display=swap" rel="stylesheet">
<style>
  :root{
    --dark-blue:#23285e;
    --light-blue:#1a97c3;
    --sky:#5cc3ea;
    --deep:#0d5f9c;
    --paper:#ffffff;
    --canvas:#e9edf1;
    --body:#3a3f4a;
  }
  *{box-sizing:border-box;margin:0;padding:0}
  html,body{width:1200px;height:2400px;overflow:hidden;background:var(--canvas);font-family:"Arimo",Arial,Helvetica,sans-serif;color:var(--body)}
  .stage{position:relative;width:1200px;height:2400px}
  .page{position:absolute;background:var(--paper);box-shadow:0 6px 22px rgba(20,40,80,.18);overflow:hidden}

  /* cover */
  .cover{background:linear-gradient(180deg,#eaf6fc 0%,#bfe5f6 14%,var(--sky) 32%,var(--light-blue) 60%,var(--deep) 100%)}
  .cover-logo{position:absolute;left:7%;top:4.5%;display:flex;align-items:center;gap:8px;color:var(--dark-blue);font-weight:700}
  .cover-logo .dot{background:var(--light-blue);border-radius:50%}
  .cover-art{position:absolute;left:0;right:0;top:15%;height:55%;background:radial-gradient(ellipse at 40% 40%,#e6f7ff 0%,#8fd5f1 35%,#2b9fd2 70%,#1478b2 100%)}
  .cover-title{position:absolute;left:0;right:0;top:72%;text-align:right;padding-right:7%;color:#fff;font-weight:700;letter-spacing:.5px}
  .cover-foot{position:absolute;left:0;right:0;bottom:4%;text-align:center;color:#d8effa;line-height:1.5}

  .cover-main{left:340px;top:64px;width:520px;height:672px}
  .cover-main .cover-logo{font-size:26px}
  .cover-main .cover-logo .dot{width:20px;height:20px}
  .cover-main .cover-title{font-size:30px}
  .cover-main .cover-foot{font-size:11px}

  .spread{position:absolute;left:50px;width:1100px;height:712px;display:flex;box-shadow:0 6px 22px rgba(20,40,80,.18)}
  .spread .page{position:relative;width:550px;height:712px;box-shadow:none}
  .spread .page+.page{border-left:1px solid #d9e1e8}
  .inside{top:820px}
  .outside{top:1620px}

  .inner{padding:40px 38px 0}
  .inner p{font-size:11px;line-height:1.5;margin-bottom:9px}
  .inner h2{font-size:13px;color:var(--dark-blue);margin:14px 0 6px}
  .inner ul{list-style:none;margin:0 0 10px 12px}
  .inner li{font-size:11px;line-height:1.5;padding-left:12px;position:relative}
  .inner li::before{content:"";position:absolute;left:0;top:6px;width:5px;height:5px;background:var(--light-blue)}
  .brand{color:var(--light-blue);font-weight:700}

  .feature{display:flex;gap:16px;margin-bottom:22px}
  .feature-photo{flex:0 0 150px;height:150px;background:linear-gradient(135deg,#bfe6f7,#2a9fd1 60%,var(--dark-blue))}
  .feature h2{margin-top:0;display:flex;align-items:center;gap:7px}
  .feature h2::before{content:"";width:8px;height:8px;background:var(--light-blue)}

  .bar{position:absolute;left:0;right:0;bottom:0;height:46px;display:flex;align-items:center;justify-content:space-between;padding:0 30px;background:linear-gradient(90deg,var(--light-blue),#ffffff)}
  .bar .contact{color:var(--dark-blue);font-size:10px;line-height:1.4}
  .bar .mark{display:flex;align-items:center;gap:6px;color:var(--dark-blue);font-weight:700;font-size:15px}
  .bar .mark .dot{width:10px;height:10px;border-radius:50%;background:var(--light-blue)}

  .back{background:linear-gradient(180deg,#eaf6fc 0%,var(--sky) 45%,var(--light-blue) 100%)}
  .back-text{position:absolute;left:0;right:0;bottom:60px;text-align:center;color:#fff;font-size:11px;line-height:1.6}
  .outside .cover .cover-logo{font-size:27px}
  .outside .cover .cover-logo .dot{width:20px;height:20px}
  .outside .cover .cover-title{font-size:31px}
  .outside .cover .cover-foot{font-size:11px}
</style>
</head>
<body>
<main class="stage">

  <!-- Front cover -->
  <section class="page cover cover-main">
    <div class="cover-logo"><span class="dot"></span>Northdesk</div>
    <div class="cover-art" role="img" aria-label="Concept illustration of bright blue arrows weaving through a maze of paths"></div>
    <h1 class="cover-title">iLUMO Automated Workflow</h1>
    <p class="cover-foot">Northdesk Inc. · 400 Harbor Lane, Suite 12 · Lakeview, CA 90000<br>Tel 555.010.2040 · www.northdesk.example</p>
  </section>

  <!-- Inside spread -->
  <section class="spread inside">
    <article class="page">
      <div class="inner">
        <p><span class="brand">Northdesk</span> is one of the leading providers of back office workflow and document solutions for independent broker dealers and RIAs. Our platform brings automated processing, secure storage and real time visibility to every step of the account lifecycle, helping firms serve clients faster.</p>
        <h2>Features/Benefits</h2>
        <ul>
          <li>Reduce overall costs of paperwork processing</li>
          <li>Faster account opening</li>
          <li>Improved data accuracy</li>
          <li>Secure document storage</li>
          <li>Full audit trail and reporting</li>
          <li>Fully integrated with existing custodian systems</li>
        </ul>
        <h2>What is Northdesk Transition Services/iLUMO Automation Workflow</h2>
        <p>The iLUMO workflow connects advisors, operations staff and custodians on one shared platform. Forms are captured once, checked automatically and routed to the right reviewer, so no file sits idle and nothing gets lost along the way.</p>
        <ul>
          <li>Electronic forms with built in validation rules</li>
          <li>Automated routing to operations and compliance</li>
          <li>Status tracking from submission to approval</li>
          <li>Direct submission to the clearing firm</li>
        </ul>
        <p>iLUMO scales with your business, whether you support a small team or thousands of advisors across many branch offices.</p>
        <h2>Background</h2>
        <p>Firms moving to a new custodian face a large volume of paperwork in a short window. Our transition team handles the heavy lifting so advisors can stay focused on clients.</p>
        <ul>
          <li>Build a Better Connection with Clients</li>
          <li>Reduce Costs and Improve Efficiencies</li>
          <li>Protect Your Data and Your Firm</li>
        </ul>
        <p>Northdesk provides a secure and compliant electronic process without a heavy IT footprint.</p>
      </div>
    </article>
    <article class="page">
      <div class="inner">
        <div class="feature">
          <div class="feature-photo" role="img" aria-label="Photo of an advisor meeting with clients"></div>
          <div>
            <h2>Build a Better Connection with Clients</h2>
            <p>By reducing the time spent on paperwork, advisors can spend more hours with clients and less time chasing forms. Accounts open in days rather than weeks.</p>
            <p>Clients see a faster, more professional experience from the very first meeting, which builds trust and lasting relationships.</p>
          </div>
        </div>
        <div class="feature">
          <div class="feature-photo" role="img" aria-label="Photo of a business team working at a computer"></div>
          <div>
            <h2>Reduce Costs and Improve Efficiencies</h2>
            <p>Automated checks catch missing signatures and errors before submission, cutting rework and not in good order items across the office.</p>
            <p>Printing, shipping and storage costs fall sharply while staff handle more accounts with the same resources.</p>
          </div>
        </div>
        <div class="feature">
          <div class="feature-photo" role="img" aria-label="Photo of a secure data lock concept"></div>
          <div>
            <h2>Protect Your Data and Your Firm</h2>
            <p>All documents are encrypted in transit and at rest, with access controls that match your compliance policy and a full record of every action.</p>
            <p>Supervisors review items from anywhere, and audits are answered in minutes instead of days.</p>
          </div>
        </div>
      </div>
      <div class="bar">
        <div class="contact">555.010.2040<br>info@northdesk.example</div>
        <div class="mark"><span class="dot"></span>Northdesk</div>
      </div>
    </article>
  </section>

  <!-- Outside spread -->
  <section class="spread outside">
    <article class="page back">
      <p class="back-text">Northdesk Inc.<br>400 Harbor Lane, Suite 12 · Lakeview, CA 90000<br>Tel 555.010.2040 · www.northdesk.example</p>
    </article>
    <article class="page cover">
      <div class="cover-logo"><span class="dot"></span>Northdesk</div>
      <div class="cover-art" role="img" aria-label="Concept illustration of bright blue arrows weaving through a maze of paths"></div>
      <h1 class="cover-title">iLUMO Automated Workflow</h1>
      <p class="cover-foot">Northdesk Inc. · 400 Harbor Lane, Suite 12 · Lakeview, CA 90000<br>Tel 555.010.2040 · www.northdesk.example</p>
    </article>
  </section>

</main>
</body>
</html>
```